New design for www.tolvadera.com

New Web design for www.tolvadera.com.

We strongly encourage to see the actual design, and make proposal, as we find the best proyect we can increase the budget if necessary.
Wordpress, Joomla... not a problem

Best regards

Benedict
Updates

More time, for better proyect choice

Enfermo

Enfermo

Enfermo

Target Market(s)

Industria alimentaria, Zelkor clients, government organization

Industry/Entity Type

Food blog

Coding

Coded - Design and coding required

Number of Pages Required

5+ page

Font styles to use
Sans Serif

Requirements
Must have
• Facebook and Instagram link
Whatsapp API to direct message
Great design (we process cereal as amaranth and quinoa)
Nice to have
• See the actual section in the original webpage.

```html
<!DOCTYPE html>
<html lang="en">
<head>
<meta charset="utf-8">
<title>Tolvadera</title>
<link href="https://fonts.googleapis.com/css2?family=Lato:wght@400;700;900&display=swap" rel="stylesheet">
<style>
:root{
  --red:#e8332b;
  --red-deep:#d9261f;
  --orange:#f58a1f;
  --yellow:#f7b500;
  --ink:#222222;
  --text:#555555;
  --white:#ffffff;
  --black:#151515;
  --green:#22c55e;
  --paper:#f3f3f4;
}
*{box-sizing:border-box;margin:0;padding:0}
html,body{width:1200px;height:3622px;overflow:hidden;background:var(--white)}
body{font-family:'Lato',sans-serif;color:var(--text)}
.page{position:relative;width:1200px;height:3622px;overflow:hidden}
.abs{position:absolute}

/* hero */
.hero-photo{left:0;top:0;width:1200px;height:760px;
  background:linear-gradient(180deg,#6f8fb8 0%,#8fa7c4 14%,#6d7a55 22%,#8a7a2e 40%,#a57f22 60%,#7a5a1c 100%)}
.pack-photo{left:633px;top:176px;width:478px;height:380px;border-radius:18px;
  background:linear-gradient(135deg,#f4f1ec 0%,#e9e4dc 60%,#d8cfc1 100%)}
.brand-top{left:112px;top:30px;display:flex;align-items:center;gap:12px;color:var(--white);font-size:30px;font-weight:700}
.brand-top .dot{width:34px;height:34px;border-radius:50%;background:var(--white)}
.topbar{right:112px;top:22px;color:var(--white);font-size:17px;display:flex;align-items:center;gap:8px}
.topbar svg{width:14px;height:14px}
.nav{right:112px;top:72px;display:flex;gap:25px;color:var(--white);font-size:16.5px;font-weight:700;text-transform:uppercase}
.hero-title{left:110px;top:186px;color:var(--white);font-size:58px;font-weight:900;line-height:62px}
.hero-btn{left:112px;top:402px;width:207px;height:68px;border:2px solid var(--white);border-radius:34px;color:var(--white);
  font-size:19px;font-weight:700;display:flex;align-items:center;justify-content:center}
.arrow{top:318px;width:28px;height:40px}
.wave-top{left:0;top:540px;width:1200px;height:230px}

/* welcome */
.oats-photo{left:0;top:640px;width:270px;height:420px;border-radius:0 50% 50% 0;
  background:radial-gradient(circle at 40% 45%,#efe3c8 0%,#e6d2a6 45%,rgba(255,255,255,0) 75%)}
.h2{color:var(--ink);font-weight:700;text-transform:uppercase}
.welcome-title{left:0;width:1200px;top:766px;text-align:center;font-size:44px}
.lead{left:260px;width:680px;top:832px;text-align:center;font-size:17px;line-height:26px}
.pillar{top:960px;text-align:center}
.pillar svg{width:110px;height:110px}
.pillar h3{margin-top:20px;font-size:22px;color:#333;font-weight:700}
.pillar p{margin-top:12px;font-size:16.5px;line-height:24px}

/* product sections */
.commercial{left:0;top:1291px;width:1200px;height:512px;background:var(--paper)}
.grains-photo{left:0;top:1291px;width:660px;height:512px;
  background:linear-gradient(135deg,#cfc5b3 0%,#b68a52 40%,#8b5a2b 70%,#4b2e1c 100%)}
.social{left:0;top:1803px;width:1200px;height:514px;background:linear-gradient(90deg,#f2f2f4 0%,#eeeff2 100%)}
.milk-photo{left:506px;top:1803px;width:694px;height:514px;
  background:radial-gradient(ellipse at 35% 50%,#fbf8f1 0%,#efe8da 45%,#ddd0b4 75%,#e9e7e4 100%)}
.block-title{font-size:42px;line-height:50px}
.block-sub{color:var(--red);font-size:22px;margin-top:10px}
.block-text{font-size:16.5px;line-height:26px;margin-top:20px;width:385px}
.btn-yellow{display:inline-flex;align-items:center;justify-content:center;margin-top:30px;height:56px;width:188px;
  border-radius:28px;background:var(--yellow);color:var(--white);font-weight:700;font-size:17px;text-transform:uppercase}

/* call */
.call{left:0;top:2317px;width:1200px;height:338px;
  background:linear-gradient(180deg,#ec3a30 0%,#e8332b 55%,#f04a34 100%)}
.call-title{left:0;width:1200px;top:2375px;text-align:center;color:var(--white);font-size:42px;font-weight:900;text-transform:uppercase}
.field{top:2460px;width:307px;height:33px;border-bottom:1.5px solid rgba(255,255,255,.85);color:var(--white);font-size:16px;font-weight:700}
.send{left:537px;top:2535px;width:126px;height:52px;border-radius:26px;background:var(--yellow);color:var(--white);
  font-size:19px;font-weight:700;display:flex;align-items:center;justify-content:center}

/* certificates */
.cert-title{left:0;width:1200px;top:2712px;text-align:center;font-size:42px}
.cert-text{left:255px;width:690px;top:2778px;text-align:center;font-size:16.5px;line-height:26px}
.badge{background:#d4d4d4}

/* footer */
.wave-foot{left:0;top:3040px;width:1200px;height:220px}
.footer{left:0;top:3230px;width:1200px;height:392px;background:var(--black)}
.foot-brand{left:110px;top:3300px;display:flex;flex-direction:column;align-items:center;gap:14px}
.foot-brand .mark{width:92px;height:92px;border-radius:50%;background:var(--yellow)}
.foot-brand span{color:var(--red);font-size:52px;font-weight:900}
.foot-col{top:3284px;color:var(--white);font-size:16px;line-height:24.6px}
.foot-col h4{font-size:17px;font-weight:700;text-transform:uppercase;margin-bottom:18px}
.contact-line{display:flex;gap:9px;align-items:flex-start;margin-bottom:25px}
.contact-line svg{width:13px;height:14px;margin-top:5px;flex:none}
.rule{left:112px;top:3524px;width:976px;height:1px;background:#3a3a3a}
.copy{left:112px;top:3560px;color:var(--white);font-size:16.5px}
.social-dot{top:3546px;width:48px;height:48px;border:1.5px solid var(--white);border-radius:50%}
.chat{left:1121px;top:3504px;width:56px;height:56px;border-radius:50%;background:var(--green)}
</style>
</head>
<body>
<div class="page">

  <!-- hero -->
  <div class="abs hero-photo" role="img" aria-label="Field of ripe quinoa and amaranth with mountains under a blue sky"></div>
  <div class="abs pack-photo" role="img" aria-label="Two Granovia flour packages, quinoa and other products"></div>
  <div class="abs brand-top"><span class="dot"></span>Tolvadera</div>
  <div class="abs topbar">
    <svg viewBox="0 0 24 24" fill="#f7b500"><path d="M6.6 10.8a15 15 0 0 0 6.6 6.6l2.2-2.2a1 1 0 0 1 1-.25 11.4 11.4 0 0 0 3.6.57 1 1 0 0 1 1 1V20a1 1 0 0 1-1 1A17 17 0 0 1 3 4a1 1 0 0 1 1-1h3.5a1 1 0 0 1 1 1c0 1.25.2 2.45.57 3.6a1 1 0 0 1-.25 1z"/></svg>
    <span>(+51) 054-318260</span><span>|</span>
    <svg viewBox="0 0 24 24" fill="#f7b500"><path d="M2 5h20v14H2z"/><path d="M2 5l10 8 10-8" stroke="#8fa7c4" stroke-width="2" fill="none"/></svg>
    <span>comercial@tolvadera.com</span>
  </div>
  <nav class="abs nav"><span>The Business</span><span>Products</span><span>Work</span><span>Points of Sale</span><span>Gallery</span><span>Contact</span></nav>
  <h1 class="abs hero-title">Quality,<br>Low Prices,<br>Innovative Products</h1>
  <div class="abs hero-btn">EXPLORE NOW!</div>
  <svg class="abs arrow" style="left:40px" viewBox="0 0 28 40"><path d="M20 6L8 20l12 14" stroke="#fff" stroke-width="4" fill="none"/></svg>
  <svg class="abs arrow" style="left:1132px" viewBox="0 0 28 40"><path d="M8 6l12 14L8 34" stroke="#fff" stroke-width="4" fill="none"/></svg>
  <svg class="abs wave-top" viewBox="0 0 1200 230" preserveAspectRatio="none">
    <path d="M0 120 C220 20 420 40 640 120 C850 200 1020 150 1200 80 L1200 230 L0 230 Z" fill="#e8332b"/>
    <path d="M0 108 C220 10 420 30 640 108 C850 186 1020 136 1200 66 L1200 230 L0 230 Z" fill="#f58a1f"/>
    <path d="M0 118 C220 20 420 40 640 118 C850 196 1020 146 1200 76 L1200 230 L0 230 Z" fill="#f7b500"/>
    <path d="M0 150 C220 40 420 60 640 140 C850 220 1020 172 1200 112 L1200 230 L0 230 Z" fill="#e8332b"/>
    <path d="M0 162 C220 54 420 72 640 154 C850 230 1020 184 1200 124 L1200 230 L0 230 Z" fill="#ffffff"/>
  </svg>

  <!-- welcome -->
  <div class="abs oats-photo" role="img" aria-label="Bowl of rolled oats spilling onto a white table"></div>
  <h2 class="abs h2 welcome-title">Welcome to Tolvadera</h2>
  <p class="abs lead">We are an agro-industrial company belonging to the food sector that is dedicated to the manufacture and marketing of cereal-based foods, for human consumption destined for the glass of milk program and the general public.</p>

  <div class="abs pillar" style="left:90px;width:330px">
    <svg viewBox="0 0 110 110" fill="none">
      <circle cx="50" cy="60" r="42" stroke="#e8332b" stroke-width="5"/>
      <circle cx="50" cy="60" r="28" stroke="#e8332b" stroke-width="5"/>
      <circle cx="50" cy="60" r="13" stroke="#e8332b" stroke-width="5"/>
      <path d="M50 60L92 18" stroke="#f7b500" stroke-width="5"/>
      <path d="M86 8l2 14 14 2-12 10-12-2-2-12z" fill="#f7b500"/>
    </svg>
    <h3>MISSION</h3>
    <p>We are committed to providing innovative food products to different markets under the same quality systems.</p>
  </div>
  <div class="abs pillar" style="left:445px;width:310px">
    <svg viewBox="0 0 110 110" fill="none">
      <path d="M10 30V10h20M80 10h20v20M100 80v20H80M30 100H10V80" stroke="#f7b500" stroke-width="4"/>
      <path d="M6 55C25 28 85 28 104 55C85 82 25 82 6 55Z" stroke="#e8332b" stroke-width="5"/>
      <circle cx="55" cy="55" r="16" stroke="#f7b500" stroke-width="5"/>
      <path d="M55 20V90M20 55H90" stroke="#e8332b" stroke-width="4"/>
    </svg>
    <h3>VISION</h3>
    <p>To be the best company that produces food destined for social food programs, in the south of the country.</p>
  </div>
  <div class="abs pillar" style="left:810px;width:270px">
    <svg viewBox="0 0 110 110" fill="none">
      <rect x="8" y="70" width="12" height="32" stroke="#e8332b" stroke-width="4"/>
      <rect x="28" y="58" width="12" height="44" stroke="#e8332b" stroke-width="4"/>
      <rect x="48" y="46" width="12" height="56" stroke="#e8332b" stroke-width="4"/>
      <path d="M8 55L40 30L58 40L86 10M74 10h12v12" stroke="#e8332b" stroke-width="4"/>
      <circle cx="74" cy="78" r="14" stroke="#f7b500" stroke-width="5" stroke-dasharray="6 3"/>
      <circle cx="96" cy="56" r="9" stroke="#f7b500" stroke-width="4" stroke-dasharray="4 2"/>
    </svg>
    <h3>VALUES</h3>
    <p>Our activities are focused on the satisfaction and well-being of our customers and collaborators.</p>
  </div>

  <!-- commercial products -->
  <div class="abs commercial"></div>
  <div class="abs grains-photo" role="img" aria-label="Wooden bowls of rice, quinoa, corn grits and chickpeas with a wooden scoop"></div>
  <div class="abs" style="left:687px;top:1375px">
    <h2 class="h2 block-title">Commercial<br>Products</h2>
    <p class="block-sub">Variety of products at your service</p>
    <p class="block-text">Duis aute irure dolor in reprehenderit in voluptate velit esse cillum dolore eu fugiat nulla pariatur xce pteur sint occaecat cupidatat non proident, sunt in culpa qui officia deserunt mollit.</p>
    <span class="btn-yellow">View Products</span>
  </div>

  <!-- social programs -->
  <div class="abs social"></div>
  <div class="abs milk-photo" role="img" aria-label="Two glasses of cereal milk drink beside a scoop of oats"></div>
  <div class="abs" style="left:111px;top:1888px">
    <h2 class="h2 block-title">Social Programs<br>Products</h2>
    <p class="block-sub">Quality products for everyone</p>
    <p class="block-text">Duis aute irure dolor in reprehenderit in voluptate velit esse cillum dolore eu fugiat nulla pariatur xce pteur sint occaecat cupidatat non proident, sunt in culpa qui officia deserunt mollit.</p>
    <span class="btn-yellow">View Products</span>
  </div>

  <!-- call form -->
  <div class="abs call" role="img" aria-label="Red-toned field of amaranth plants"></div>
  <h2 class="abs call-title">Do you want us to call you?</h2>
  <div class="abs field" style="left:104px">Name:</div>
  <div class="abs field" style="left:447px">Email:</div>
  <div class="abs field" style="left:789px">Phone No:</div>
  <div class="abs send">SEND</div>

  <!-- certificates -->
  <h2 class="abs h2 cert-title">Company Certificate</h2>
  <p class="abs cert-text">We are an industrial company belonging to the food sector that has the certifications that allow us to prevent and control risk factors that guarantee the safety of the inputs used, thus guaranteeing the quality of our products.</p>
  <div class="abs badge" style="left:243px;top:2925px;width:193px;height:68px;border-radius:6px" role="img" aria-label="Agricultural health certification badge"></div>
  <div class="abs badge" style="left:560px;top:2896px;width:130px;height:130px;border-radius:50%" role="img" aria-label="Food safety certification seal"></div>
  <div class="abs badge" style="left:805px;top:2912px;width:152px;height:98px;border-radius:6px" role="img" aria-label="Health ministry certification badge"></div>

  <!-- footer -->
  <svg class="abs wave-foot" viewBox="0 0 1200 220" preserveAspectRatio="none">
    <path d="M0 90 C200 10 420 30 640 110 C860 190 1040 120 1200 40 L1200 220 L0 220 Z" fill="#e8332b"/>
    <path d="M0 102 C200 24 420 44 640 122 C860 200 1040 134 1200 54 L1200 220 L0 220 Z" fill="#f58a1f"/>
    <path d="M0 114 C200 38 420 58 640 134 C860 212 1040 148 1200 68 L1200 220 L0 220 Z" fill="#f7b500"/>
    <path d="M0 126 C200 52 420 72 640 146 C860 220 1040 162 1200 82 L1200 220 L0 220 Z" fill="#ffffff"/>
    <path d="M0 146 C200 74 420 94 640 166 C860 236 1040 182 1200 104 L1200 220 L0 220 Z" fill="#151515"/>
  </svg>
  <div class="abs footer"></div>
  <div class="abs foot-brand"><span class="mark"></span><span>Tolvadera</span></div>

  <div class="abs foot-col" style="left:435px">
    <h4>Quick Links</h4>
    <div>The Business</div><div>Products</div><div>Work</div><div>Points Of Sale</div><div>Gallery</div><div>Contact</div>
  </div>
  <div class="abs foot-col" style="left:611px">
    <h4>Contact Us</h4>
    <div class="contact-line"><svg viewBox="0 0 24 24" fill="#f7b500"><path d="M12 2a7 7 0 0 0-7 7c0 5 7 13 7 13s7-8 7-13a7 7 0 0 0-7-7zm0 9.5A2.5 2.5 0 1 1 12 6.5a2.5 2.5 0 0 1 0 5z"/></svg><span>Alder Street Mz B4 Lot 7 Sector Linde<br>&nbsp;Valle Norte - Orvana</span></div>
    <div class="contact-line"><svg viewBox="0 0 24 24" fill="#f7b500"><path d="M6.6 10.8a15 15 0 0 0 6.6 6.6l2.2-2.2a1 1 0 0 1 1-.25 11.4 11.4 0 0 0 3.6.57 1 1 0 0 1 1 1V20a1 1 0 0 1-1 1A17 17 0 0 1 3 4a1 1 0 0 1 1-1h3.5a1 1 0 0 1 1 1c0 1.25.2 2.45.57 3.6a1 1 0 0 1-.25 1z"/></svg><span>(+51) 054-318260 I 054-592047 / (+51) 931475286</span></div>
    <div class="contact-line"><svg viewBox="0 0 24 24" fill="#f7b500"><path d="M2 5h20v14H2z"/><path d="M2 5l10 8 10-8" stroke="#151515" stroke-width="2" fill="none"/></svg><span>comercial@tolvadera.com / administracion@tolvadera.com</span></div>
  </div>

  <div class="abs rule"></div>
  <div class="abs copy">Copyright © 2021 - Tolvadera | All rights reserved</div>
  <a class="abs social-dot" style="left:983px" aria-label="Social profile"></a>
  <a class="abs social-dot" style="left:1040px" aria-label="Photo profile"></a>
  <div class="abs chat" aria-label="Direct message"></div>
</div>
</body>
</html>
```